Business card for Les Brisants-Corail campsite

HORIZONTAL / 85x55
OBJECTIVE
Create a modern, attractive and memorable business card for the Les Brisants-Corail campsite, located on the Île d'Oléron.
The map should make people want to discover the campsite and immediately convey its world: ocean, holidays, nature and conviviality.
VISUAL IDENTITY
The design must be in the same graphic style as our website:
www.lesbrisants-corail.fr
The site is the main reference for the visual atmosphere: colours, typography, shapes, photographs and general universe.
The map and the site must give the impression of belonging to a single brand identity.
A UNIVERSE TO TRANSMIT
• Île d'Oléron
• Atlantic Ocean
• Seaside
• Direct access to the beaches
• Vacation
• Nature
• Family-friendly and welcoming atmosphere
• Relaxation
DESIRED STYLE
Bright, warm, modern, nautical and natural.
We want a creation with a real personality, immediately recognizable, and not a generic camping business card.
FRONT
Prioritize visual impact with:
• Official logo Les Brisants-Corail
• Île d'Oléron
• A strong evocation of the ocean and holidays
• A short and memorable hook
The designer is free to propose their own hook.
BACK
The Coral Breakers
Villages 1 & 2
22 Rue des Mouettes
17310 Saint-Pierre-d'Oléron
France
Tel.: +33 5 47 12 38 04
www.lesbrisants-corail. fr
Possibility of discreet integration:
Direct access to the beaches
Mobile homes • Pitches • Accommodation
Le Varech Bar-Restaurant
FORMAT
Double-sided card: 85 × 55 mm.
Horizontal orientation
AVOID
• Overly institutional design
• Overloaded map
• Generic "camping" style
• Too many pictograms
• Accumulation of texts
• Modification or distortion of the official logo
• Graphic design unrelated to the website
CREATIVE FREEDOM
We are looking for an original proposal.
The designer can play with the graphic codes of the ocean, waves, sun, beach and Île d'Oléron, while remaining faithful to the visual identity of the site.
The card must be aesthetically pleasing and original enough to make people want to keep it.
The objective:
See the map → think about the ocean and holidays → remember Les Brisants-Corail → discover the campsite.
Target Market(s)
All targets
Industry/Entity Type
Tourisme
Contact Information for Business Card
adresse, téléphone, email, site internet + réseaux sociaux
Look and feel
Each slider illustrates characteristics of the customer's brand and the style your logo design should communicate.

```html
<!DOCTYPE html>
<html lang="fr">
<head>
<meta charset="utf-8">
<title>Les Brisants-Corail — carte de visite</title>
<link rel="stylesheet" href="https://fonts.googleapis.com/css2?family=DM+Serif+Display&family=Nunito:wght@500;600;700;800&display=swap">
<style>
  :root{
    --bg:#0b1f38;
    --navy:#1c2a3d;
    --green:#a2c224;
    --blue:#29a8dc;
    --sky:#d6f4fb;
    --white:#ffffff;
    --teal:#5fb7b7;
  }
  *{margin:0;padding:0;box-sizing:border-box}
  html,body{width:1200px;height:1200px;overflow:hidden}
  body{background:radial-gradient(ellipse at 50% 55%,#103a66 0%,var(--bg) 75%);font-family:"Nunito",sans-serif;position:relative}
  .card{position:absolute;left:197px;width:806px;height:522px;border-radius:32px;overflow:hidden}
  .card--front{top:56px}
  .card--back{top:610px;background:var(--white)}
  .photo{position:absolute;inset:0;background:
      linear-gradient(180deg,rgba(0,0,0,0) 55%,rgba(20,40,20,.55) 100%),
      linear-gradient(100deg,#9fb9c7 0%,#5f97ad 30%,#2c6f96 55%,#1c5a8c 75%,#245f96 100%);}
  .photo::after{content:"";position:absolute;left:0;right:0;top:52%;bottom:0;
      background:linear-gradient(180deg,#5c7a58 0%,#3d5a3a 60%,#2f4730 100%);
      clip-path:polygon(0 20%,35% 10%,70% 35%,88% 55%,90% 100%,0 100%)}
  .abs{position:absolute}
  .brand{font-family:"Nunito",sans-serif;font-weight:800;white-space:nowrap}
  .brand-mark{display:inline-block;border-radius:50%;vertical-align:middle}
  .front-brand{left:47px;top:110px;display:flex;align-items:center;gap:12px;color:var(--white);font-size:30px}
  .front-brand .brand-mark{width:40px;height:40px;background:var(--green)}
  .hook{font-family:"DM Serif Display",serif;color:var(--white);text-align:right;right:62px;top:62px;font-size:30px;line-height:27px}
  .island{font-family:"DM Serif Display",serif;color:var(--white);right:58px;top:138px;font-size:96px;line-height:96px}
  .ocean{font-family:"DM Serif Display",serif;color:var(--green);left:84px;top:384px;font-size:80px;line-height:80px;white-space:nowrap}
  .feet{font-family:"DM Serif Display",serif;color:var(--white);left:123px;top:452px;font-size:38px;line-height:40px;white-space:nowrap}

  .wave{position:absolute;inset:0}
  .back-brand{left:67px;display:flex;flex-direction:column;gap:6px}
  .back-brand .name{color:var(--navy);font-size:22px;display:flex;align-items:center;gap:8px}
  .back-brand .brand-mark{width:26px;height:26px;background:var(--blue)}
  .pill{align-self:flex-end;color:var(--white);font-size:9px;font-weight:700;letter-spacing:2px;padding:2px 14px;border-radius:8px}
  .pill--blue{background:var(--blue)}
  .pill--green{background:var(--green)}
  .contact{left:331px;display:flex;align-items:flex-start;gap:16px;color:var(--navy);font-weight:600;font-size:24px;line-height:30px;white-space:nowrap}
  .contact .ico{width:32px;height:32px;border-radius:50%;flex:none;display:flex;align-items:center;justify-content:center;margin-top:-1px}
  .ico--blue{background:var(--blue)}
  .ico--yellow{background:#f2e356}
  .ico--green{background:var(--green)}
  .beach-a{font-family:"DM Serif Display",serif;color:var(--green);font-size:28px;right:459px;top:350px;text-align:right;white-space:nowrap}
  .beach-b{font-family:"DM Serif Display",serif;color:var(--blue);font-size:42px;right:459px;top:374px;white-space:nowrap}
  .offers{left:367px;top:360px;list-style:none;font-family:"DM Serif Display",serif;color:var(--navy);font-size:16px;line-height:21px;white-space:nowrap}
  .offers li::before{content:"★";color:var(--blue);font-size:11px;margin-right:9px;vertical-align:2px}
  .resto-tag{left:554px;top:302px;font-family:"DM Serif Display",serif;font-size:17px;line-height:20px;color:var(--green);white-space:nowrap}
  .resto-tag span{color:var(--blue)}
  .resto{left:554px;top:354px;white-space:nowrap}
  .resto .name{font-family:"Nunito",sans-serif;font-weight:800;color:var(--navy);font-size:32px;letter-spacing:1px;line-height:36px}
  .resto .sub{font-size:12px;letter-spacing:3.6px;color:var(--navy);border-bottom:2px solid var(--teal);padding-bottom:2px;margin-top:6px;line-height:14px}
  .url{left:82px;top:450px;font-weight:700;font-size:22px;letter-spacing:1px;color:var(--navy);white-space:nowrap}
  .social{left:471px;top:456px;display:flex;align-items:center;gap:6px;font-weight:800;font-size:16px;color:var(--navy);white-space:nowrap}
  .social .dot{width:23px;height:23px;border-radius:50%;background:var(--green)}
  .social .label{margin-right:6px}
</style>
</head>
<body>
  <section class="card card--front">
    <div class="photo" role="img" aria-label="Vue aérienne du camping en bord d'océan, côte de l'île d'Oléron avec contour de l'île et vague déferlante"></div>
    <div class="abs front-brand brand"><span class="brand-mark"></span>Les Brisants-Corail</div>
    <p class="abs hook">Un séjour les pieds<br>dans l’eau<br>sur l’île</p>
    <p class="abs island">d’Oléron</p>
    <p class="abs ocean">L’océan</p>
    <p class="abs feet">à vos pieds !</p>
  </section>

  <section class="card card--back">
    <svg class="wave" viewBox="0 0 806 522" preserveAspectRatio="none" aria-hidden="true">
      <path d="M0,258 C150,345 330,330 500,272 C640,228 740,255 806,305 L806,522 L0,522Z" fill="var(--sky)"/>
      <path d="M0,258 C150,345 330,330 500,272 C640,228 740,255 806,305" fill="none" stroke="var(--blue)" stroke-width="6"/>
    </svg>

    <div class="abs back-brand" style="top:62px">
      <div class="name brand"><span class="brand-mark"></span>Les Brisants-Corail</div>
      <span class="pill pill--blue">VILLAGE 1</span>
    </div>
    <div class="abs back-brand" style="top:177px">
      <div class="name brand"><span class="brand-mark" style="background:var(--green)"></span>Les Brisants-Corail</div>
      <span class="pill pill--green">VILLAGE 2</span>
    </div>

    <div class="abs contact" style="top:70px">
      <span class="ico ico--blue"><svg width="16" height="16" viewBox="0 0 24 24"><path d="M6.6 10.8a15 15 0 0 0 6.6 6.6l2.2-2.2a1 1 0 0 1 1-.25 11.4 11.4 0 0 0 3.6.57 1 1 0 0 1 1 1V20a1 1 0 0 1-1 1A17 17 0 0 1 3 4a1 1 0 0 1 1-1h3.5a1 1 0 0 1 1 1c0 1.25.2 2.45.57 3.57a1 1 0 0 1-.25 1z" fill="#fff"/></svg></span>
      <span>+33 5 47 12 38 04</span>
    </div>
    <div class="abs contact" style="top:115px">
      <span class="ico ico--yellow"><svg width="18" height="14" viewBox="0 0 18 14"><rect x="1" y="1" width="16" height="12" rx="2" fill="none" stroke="#fff" stroke-width="1.8"/><path d="M1.5 2 9 8l7.5-6" fill="none" stroke="#fff" stroke-width="1.8"/></svg></span>
      <span>camping@lesbrisants-corail.fr</span>
    </div>
    <div class="abs contact" style="top:158px">
      <span class="ico ico--green"><svg width="14" height="18" viewBox="0 0 14 18"><path d="M7 1a6 6 0 0 0-6 6c0 4.5 6 10 6 10s6-5.5 6-10a6 6 0 0 0-6-6z" fill="#fff"/><circle cx="7" cy="7" r="2.3" fill="var(--green)"/></svg></span>
      <span>22 Rue des Mouettes<br>17310 Saint-Pierre-d'Oléron<br>France</span>
    </div>

    <p class="abs beach-a">Accès direct aux</p>
    <p class="abs beach-b">Plages</p>
    <ul class="abs offers">
      <li>Mobil-homes</li>
      <li>Emplacements</li>
      <li>Hébergements</li>
    </ul>

    <p class="abs resto-tag">Un goût de vacances à<br><span>chaque assiette</span></p>
    <div class="abs resto">
      <div class="name">LE VARECH</div>
      <div class="sub">BAR / RESTAURANT</div>
    </div>

    <p class="abs url">www.lesbrisants-corail.fr</p>
    <div class="abs social"><span class="label">SUIVEZ-NOUS SUR</span><span class="dot"></span><span class="dot"></span><span class="dot"></span><span class="dot"></span></div>
  </section>
</body>
</html>
```